Anchorwell Giving - New Website Designed

I need a site that looks like this http://www.lumenhavenfund.org for boat donations. So please replace the cars with boats.

```html
<!DOCTYPE html>
<html lang="en">
<head>
<meta charset="utf-8">
<title>Anchorwell Giving – Boat Donations</title>
<link href="https://fonts.googleapis.com/css2?family=Open+Sans:wght@400;600;700;800&display=swap" rel="stylesheet">
<style>
:root{
  --red:#d2213f;
  --navy:#2b2a6b;
  --navy-deep:#1d1b4c;
  --ink:#111;
  --muted:#8a8a8a;
  --pale:#f4f5f8;
  --chip:#d6d6d6;
  --white:#fff;
}
*{box-sizing:border-box;margin:0;padding:0}
html,body{width:1200px;height:3147px;overflow:hidden}
body{font-family:"Open Sans",Arial,sans-serif;color:var(--ink);background:var(--white);position:relative}
.abs{position:absolute}

/* header */
.site-header{position:absolute;top:0;left:0;width:1200px;height:142px;border-top:4px solid var(--red);background:var(--white)}
.brand{position:absolute;left:30px;top:36px;display:flex;align-items:center;gap:10px}
.brand-dot{width:40px;height:40px;border-radius:50%;background:var(--navy)}
.brand-name{font-size:22px;font-weight:700;color:var(--red);line-height:1}
.brand-tag{font-size:11px;color:var(--navy);margin-top:3px}
.call{position:absolute;right:34px;top:46px;text-align:right}
.call-label{font-size:19px;font-weight:700;color:var(--navy)}
.call-number{font-size:27px;font-weight:700;color:var(--red);margin-top:2px;display:flex;align-items:center;justify-content:flex-end;gap:10px}

/* nav */
.main-nav{position:absolute;top:142px;left:0;width:1200px;height:68px;background:var(--navy)}
.nav-item{position:absolute;top:0;height:68px;line-height:68px;color:var(--white);font-size:17px;font-weight:600;text-transform:uppercase}
.nav-item.active{background:var(--red);padding:0 14px;left:29px}
.donate-btn{position:absolute;left:959px;top:11px;width:214px;height:46px;background:var(--red);color:var(--white);font-weight:700;font-size:17px;display:flex;align-items:center;justify-content:center;gap:10px}

/* hero */
.hero{position:absolute;top:210px;left:0;width:1200px;height:531px;background:linear-gradient(120deg,#37497f 0%,#6b6f96 35%,#8a4a5c 65%,#3a2f55 100%)}
.hero-form{position:absolute;left:799px;top:42px;width:376px;height:463px;background:var(--red);padding:24px 29px 0;text-align:center;color:var(--white)}
.hero-form h2{font-size:31px;font-weight:700;letter-spacing:.5px}
.hero-form p{font-size:15px;line-height:1.3;margin-top:4px}
.field{height:44px;background:var(--white);margin-top:18px;display:flex;align-items:center;justify-content:space-between;padding:0 14px;color:#aaa;font-size:15px;font-style:italic}
.field:first-of-type{margin-top:28px}
.continue{display:block;margin:22px auto 0;width:216px;height:57px;background:var(--navy);color:var(--white);font-size:22px;font-weight:700;line-height:57px}

/* give a hand */
.section-title{font-size:34px;font-weight:800;text-transform:uppercase}
.give{position:absolute;top:741px;left:0;width:1200px;height:417px;text-align:center}
.give .section-title{position:absolute;top:50px;width:100%}
.give .lede{position:absolute;top:96px;width:100%;color:var(--muted);font-size:19px}
.hand-card{position:absolute;top:165px;width:336px;height:185px;border:1px solid #e4e4e4;background:var(--white);text-align:center}
.hand-card h3{color:var(--red);font-size:21px;font-weight:700;text-transform:uppercase}
.hand-card .bar{width:42px;height:6px;background:#444;margin:10px auto 0}
.hand-card.raised{box-shadow:4px 5px 8px rgba(0,0,0,.2)}
.hand-card.raised p{font-size:13px;color:var(--muted);line-height:1.5;margin:10px 40px 0}
.plus-ring{width:40px;height:40px;border:2px solid var(--red);border-radius:50%;color:var(--red);margin:10px auto 0;line-height:34px;font-size:22px}

/* what we do */
.what{position:absolute;top:1158px;left:0;width:1200px;height:468px;background:var(--pale)}
.what .section-title{position:absolute;left:27px;top:56px}
.underline{width:72px;height:8px;background:var(--red)}
.what .underline{position:absolute;left:29px;top:101px}
.what-item{position:absolute;left:29px;width:481px;height:46px;background:var(--chip);display:flex;align-items:center;gap:14px;padding-left:14px;font-size:20px}
.what-item.active{background:var(--red);color:var(--white)}
.what-item .dot{width:19px;height:19px;border-radius:50%;background:#333;display:flex;align-items:center;justify-content:center}
.what-item.active .dot{background:var(--white)}
.what-photo{position:absolute;left:623px;top:126px;width:544px;height:271px;background:linear-gradient(90deg,#2f3650 0%,#6d7aa0 40%,#c7c9d8 60%,#b9394e 100%)}

/* faq */
.faq{position:absolute;top:1626px;left:0;width:1200px;height:610px;background:linear-gradient(160deg,#302f72 0%,#221f55 55%,#3b244e 100%);text-align:center;color:var(--white)}
.faq .section-title{position:absolute;top:38px;width:100%;font-size:31px;font-weight:700}
.faq .underline{position:absolute;left:551px;top:92px;width:80px;background:var(--white)}
.faq-item{position:absolute;left:84px;width:1020px;height:57px;border:1.5px solid rgba(255,255,255,.55);border-radius:4px;display:flex;align-items:center;justify-content:space-between;padding:0 18px 0 18px;font-size:21px;text-align:left}
.faq-item.active{background:var(--red);border-color:var(--red);padding-left:28px}
.faq-item .plus{font-size:30px;font-weight:300}

/* events */
.events{position:absolute;top:2236px;left:0;width:1200px;height:559px}
.events-photo{position:absolute;left:27px;top:74px;width:563px;height:413px;background:linear-gradient(200deg,#dfe8f3 0%,#5a7ab0 40%,#b84552 65%,#4a4d57 100%)}
.events .section-title{position:absolute;left:657px;top:66px;font-size:33px}
.events .underline{position:absolute;left:657px;top:116px;width:86px}
.event{position:absolute;left:657px;width:516px;height:84px}
.event-thumb{position:absolute;left:0;top:0;width:140px;height:84px;background:linear-gradient(135deg,#323a59,#8a92a8 60%,#a33a4a)}
.event-date{position:absolute;left:174px;top:4px;color:var(--red);font-size:18px;display:flex;align-items:center;gap:8px}
.event-text{position:absolute;left:174px;top:34px;color:#aaa;font-size:13px;line-height:1.6;width:342px}

/* footer */
.site-footer{position:absolute;top:2795px;left:0;width:1200px;height:352px;background:var(--navy);color:var(--white);border-bottom:8px solid var(--red)}
.foot-brand{position:absolute;left:29px;top:44px}
.foot-brand .brand-dot{background:var(--white);width:46px;height:46px;margin-left:34px}
.foot-brand .brand-name{color:var(--white);font-size:20px;margin-top:6px}
.foot-about{position:absolute;left:29px;top:142px;width:260px;font-size:14px;line-height:1.5}
.foot-col{position:absolute;top:58px}
.foot-col h4{font-size:20px;font-weight:700;text-transform:uppercase;letter-spacing:.3px}
.foot-links{list-style:none;margin-top:14px;font-size:14px;line-height:29px}
.insta-grid{display:grid;grid-template-columns:repeat(4,57px);grid-template-rows:repeat(2,63px);gap:4px;margin-top:18px}
.insta-grid span{background:linear-gradient(135deg,#5c6585,#a7aec4 55%,#8f3a4f)}
.contact{list-style:none;margin-top:16px;font-size:14px;line-height:1.45}
.contact li{display:flex;gap:12px;margin-bottom:10px}
.foot-bottom{position:absolute;top:306px;font-size:13px}
.socials{position:absolute;right:29px;top:304px;display:flex;gap:6px}
.socials span{width:14px;height:14px;background:var(--white);border-radius:2px}
</style>
</head>
<body>

<header class="site-header">
  <div class="brand">
    <div class="brand-dot"></div>
    <div>
      <div class="brand-name">Anchorwell Giving</div>
      <div class="brand-tag">Giving Together</div>
    </div>
  </div>
  <div class="call">
    <div class="call-label">CALL US TO DONATE BOAT ONLINE</div>
    <div class="call-number">
      <svg width="22" height="22" viewBox="0 0 24 24"><path fill="#d2213f" d="M6.6 10.8a15.1 15.1 0 0 0 6.6 6.6l2.2-2.2a1 1 0 0 1 1-.25 11.4 11.4 0 0 0 3.6.57 1 1 0 0 1 1 1V20a1 1 0 0 1-1 1A17 17 0 0 1 3 4a1 1 0 0 1 1-1h3.5a1 1 0 0 1 1 1c0 1.25.2 2.45.57 3.57a1 1 0 0 1-.25 1z"/></svg>
      +1-555-014-2290
    </div>
  </div>
</header>

<nav class="main-nav">
  <div class="nav-item active">Home</div>
  <div class="nav-item" style="left:136px">Give a hand</div>
  <div class="nav-item" style="left:275px">What we do</div>
  <div class="nav-item" style="left:428px">Frequently asked questions</div>
  <div class="nav-item" style="left:735px">Upcoming events</div>
  <div class="donate-btn">
    <svg width="24" height="24" viewBox="0 0 24 24" fill="none" stroke="#fff" stroke-width="1.6"><path d="M2 15h4l5 2h5a2 2 0 0 0 0-4h-4"/><path d="M6 20h9l6-5"/><circle cx="15" cy="6" r="3"/></svg>
    DONATE NOW
  </div>
</nav>

<section class="hero">
  <div class="abs" role="img" aria-label="Hand holding a small blue rowing boat in front of a waving flag" style="inset:0"></div>
  <form class="hero-form">
    <h2>FILL THE FORM !</h2>
    <p>Nulla tincidunt arcu vitae quam consec-<br>tetur, eget scelerisqueS</p>
    <div class="field">enter your name
      <svg width="14" height="16" viewBox="0 0 14 16"><circle cx="7" cy="4.5" r="3.5" fill="#bbb"/><path d="M0 16c0-4 3-6 7-6s7 2 7 6z" fill="#bbb"/></svg></div>
    <div class="field">enter your e-mail
      <svg width="16" height="12" viewBox="0 0 16 12"><rect width="16" height="12" fill="#bbb"/><path d="M0 0l8 6 8-6" stroke="#fff" fill="none"/></svg></div>
    <div class="field">enter your phone no
      <svg width="15" height="15" viewBox="0 0 24 24"><path fill="#bbb" d="M6.6 10.8a15.1 15.1 0 0 0 6.6 6.6l2.2-2.2a1 1 0 0 1 1-.25 11.4 11.4 0 0 0 3.6.57 1 1 0 0 1 1 1V20a1 1 0 0 1-1 1A17 17 0 0 1 3 4a1 1 0 0 1 1-1h3.5a1 1 0 0 1 1 1c0 1.25.2 2.45.57 3.57a1 1 0 0 1-.25 1z"/></svg></div>
    <div class="field">enter your zip-code
      <svg width="10" height="6" viewBox="0 0 10 6"><path d="M0 0h10L5 6z" fill="#bbb"/></svg></div>
    <div class="continue">CONTINUE</div>
  </form>
</section>

<section class="give">
  <h2 class="section-title">Give a hand</h2>
  <p class="lede">On the other hand, we denounce with righteous indignation and dislike men who are so beguiled</p>

  <div class="hand-card" style="left:29px">
    <svg style="margin-top:26px" width="76" height="70" viewBox="0 0 76 70" fill="#2b2a6b">
      <path d="M20 70V42l-8-14 4-2 8 12V14h4v24h2V8h4v30h2V12h4v28l6-6 3 3-11 15v18z"/>
      <path d="M44 70V50l6-8 5-10 3 2-3 8h1V20h4v20h2V14h4v26h2V22h4v28l-8 20z"/>
    </svg>
    <h3 style="margin-top:18px">Become a vounter</h3>
    <div class="bar"></div>
  </div>

  <div class="hand-card raised" style="left:432px">
    <h3 style="margin-top:20px">Boat for donation</h3>
    <p>It is a long established fact that a reader will be distracted by the readable content of a page</p>
    <div class="plus-ring">+</div>
  </div>

  <div class="hand-card" style="left:835px">
    <svg style="margin-top:20px" width="72" height="82" viewBox="0 0 72 82">
      <rect x="4" y="40" width="64" height="42" fill="#2b2a6b"/>
      <rect x="14" y="40" width="44" height="6" fill="#fff"/>
      <circle cx="36" cy="30" r="11" fill="#2b2a6b" stroke="#fff" stroke-width="2"/>
      <path d="M22 4h30l10 10H30z" fill="#2b2a6b"/>
    </svg>
    <h3 style="margin-top:14px">Donation</h3>
    <div class="bar"></div>
  </div>
</section>

<section class="what">
  <h2 class="section-title">What we do</h2>
  <div class="underline"></div>
  <div class="what-item active" style="top:143px"><span class="dot"><svg width="8" height="10" viewBox="0 0 8 10"><path d="M1 1l5 4-5 4" stroke="#d2213f" stroke-width="2" fill="none"/></svg></span>Loren Ipsum Dolar Sit Amet</div>
  <div class="what-item" style="top:206px"><span class="dot"><svg width="8" height="10" viewBox="0 0 8 10"><path d="M1 1l5 4-5 4" stroke="#fff" stroke-width="2" fill="none"/></svg></span>Consiclet loren ipsum dolar</div>
  <div class="what-item" style="top:267px"><span class="dot"><svg width="8" height="10" viewBox="0 0 8 10"><path d="M1 1l5 4-5 4" stroke="#fff" stroke-width="2" fill="none"/></svg></span>Loren Ipsum Dolar Sit Amet</div>
  <div class="what-item" style="top:330px"><span class="dot"><svg width="8" height="10" viewBox="0 0 8 10"><path d="M1 1l5 4-5 4" stroke="#fff" stroke-width="2" fill="none"/></svg></span>Loren Ipsum Dolar Sit Amet</div>
  <div class="what-photo" role="img" aria-label="Silhouette of a saluting serviceman before a large flag"></div>
</section>

<section class="faq">
  <div class="abs" role="img" aria-label="Faded crowd of veterans holding flags" style="inset:0"></div>
  <h2 class="section-title">FREQUENTLY ASKED QUESTIONS</h2>
  <div class="underline"></div>
  <div class="faq-item active" style="top:136px">What Type Of Boat Can Be Donated <span class="plus">+</span></div>
  <div class="faq-item" style="top:220px">Is my donated vehicle tax-deductible? <span class="plus">+</span></div>
  <div class="faq-item" style="top:300px">What if the vehicle is not registered in my name? <span class="plus">+</span></div>
  <div class="faq-item" style="top:388px">How much will I receive as a tax deduction for my vehicle? <span class="plus">+</span></div>
  <div class="faq-item" style="top:476px">How much will I receive as a tax deduction for my vehicle? <span class="plus">+</span></div>
</section>

<section class="events">
  <div class="events-photo" role="img" aria-label="Marchers carrying a huge flag under a blue sky"></div>
  <h2 class="section-title">OUR UPCOMING EVENTS</h2>
  <div class="underline"></div>

  <div class="event" style="top:158px">
    <div class="event-thumb" role="img" aria-label="Veteran saluting beside a flag"></div>
    <div class="event-date"><svg width="16" height="16" viewBox="0 0 16 16"><rect x="1" y="3" width="14" height="12" fill="none" stroke="#d2213f" stroke-width="2"/><path d="M1 6h14M5 1v4M11 1v4" stroke="#d2213f" stroke-width="2"/></svg>21 JAN 2017</div>
    <div class="event-text">The standard chunk of Lorem Ipsum used since the 1500s is reproduced below</div>
  </div>
  <div class="event" style="top:275px">
    <div class="event-thumb" role="img" aria-label="Honour guard folding a flag"></div>
    <div class="event-date"><svg width="16" height="16" viewBox="0 0 16 16"><rect x="1" y="3" width="14" height="12" fill="none" stroke="#d2213f" stroke-width="2"/><path d="M1 6h14M5 1v4M11 1v4" stroke="#d2213f" stroke-width="2"/></svg>20 JUNE 2017</div>
    <div class="event-text">The standard chunk of Lorem Ipsum used since the 1500s is reproduced below</div>
  </div>
  <div class="event" style="top:403px">
    <div class="event-thumb" role="img" aria-label="Uniformed officers at a ceremony"></div>
    <div class="event-date"><svg width="16" height="16" viewBox="0 0 16 16"><rect x="1" y="3" width="14" height="12" fill="none" stroke="#d2213f" stroke-width="2"/><path d="M1 6h14M5 1v4M11 1v4" stroke="#d2213f" stroke-width="2"/></svg>21 AUG 2017</div>
    <div class="event-text">The standard chunk of Lorem Ipsum used since the 1500s is reproduced below</div>
  </div>
</section>

<footer class="site-footer">
  <div class="foot-brand">
    <div class="brand-dot"></div>
    <div class="brand-name">Anchorwell Giving</div>
  </div>
  <p class="foot-about">Contrary to popular belief, Lorem Ipsum is not simply random text. It has roots in a piece of classical Latin litera-ture from 45 BC, making it over 2000 years old.</p>

  <div class="foot-col" style="left:390px">
    <h4>Special links</h4>
    <ul class="foot-links"><li>About Us</li><li>Where We Work</li><li>Donate Now</li><li>Events</li></ul>
  </div>

  <div class="foot-col" style="left:602px">
    <h4>Instagram feed</h4>
    <div class="insta-grid" role="img" aria-label="Grid of eight event photos">
      <span></span><span></span><span></span><span></span><span></span><span></span><span></span><span></span>
    </div>
  </div>

  <div class="foot-col" style="left:887px">
    <h4>Get in touch with us</h4>
    <ul class="contact">
      <li><svg width="12" height="16" viewBox="0 0 12 16"><path d="M6 0a6 6 0 0 1 6 6c0 4-6 10-6 10S0 10 0 6a6 6 0 0 1 6-6z" fill="#fff"/><circle cx="6" cy="6" r="2" fill="#2b2a6b"/></svg><span>48 Harbor Lane, Suite 210<br>Portland, Maine United States</span></li>
      <li><svg width="13" height="13" viewBox="0 0 24 24"><path fill="#fff" d="M6.6 10.8a15.1 15.1 0 0 0 6.6 6.6l2.2-2.2a1 1 0 0 1 1-.25 11.4 11.4 0 0 0 3.6.57 1 1 0 0 1 1 1V20a1 1 0 0 1-1 1A17 17 0 0 1 3 4a1 1 0 0 1 1-1h3.5a1 1 0 0 1 1 1c0 1.25.2 2.45.57 3.57a1 1 0 0 1-.25 1z"/></svg><span>Phone : +15550148820</span></li>
      <li><svg width="14" height="11" viewBox="0 0 16 12"><rect width="16" height="12" fill="#fff"/><path d="M0 0l8 6 8-6" stroke="#2b2a6b" fill="none"/></svg><span>E-mail : hello@anchorwellgiving.org</span></li>
    </ul>
  </div>

  <div class="foot-bottom" style="left:31px">Copyright2017.Al Right Reserved</div>
  <div class="foot-bottom" style="left:492px">Privacy Policy | Terms &amp; Conditions |FAQ'S</div>
  <div class="socials"><span></span><span></span><span></span><span></span></div>
</footer>

</body>
</html>
```